Business Cards for a Junk Removal Company

Hello,
We are looking to have business cards designed that are simple, bold, easy to read, and right to the point. Please see the attachments for our logo files. We want the card to be yellow on both sides ( Color code Yellow: #FFE01B). The logo text font is (Rockstar Extra Bold) and this is also in the files attached. Please make the text black for the logo. On the back side of the card, you can use white and black for text. Thank you in advance for your hard work!

Front of card-
Harbor Haul Away (logo)
Back of card-
Harbor Haul Away
Donate - Recycle - Dispose
555-271-8093
www.harborhaulaway.example
info@harborhaulaway.example

Industry/Entity Type

Junk removal

Contact Information for Business Card

FRONT OF CARD- Harbor Haul Away (logo) BACK OF CARD- Harbor Haul Away Donate - Recycle - Dispose 555-271-8093 www.harborhaulaway.example info@harborhaulaway.example

Font styles to use
Other font styles liked:
• Rockstar Extra Bold

Colors
FFF300
FFF600
FEFA6F
FFFEC7
FFFEE8

Requirements
Must have
• Must have color code Yellow: #FFE01B for the background of front and back of the card

```html
<!DOCTYPE html>
<html lang="en">
<head>
<meta charset="UTF-8">
<title>Harbor Haul Away – Business Cards</title>
<link href="https://fonts.googleapis.com/css2?family=Anton&family=Arimo:wght@400&display=swap" rel="stylesheet">
<style>
  :root {
    --stage: #e9e9ea;
    --card-yellow: #FFE01B;
    --ink: #1c1c1c;
    --text-dark: #2b2b2c;
    --rule: #1c1c1c;
    --white: #ffffff;
  }
  * { margin: 0; padding: 0; box-sizing: border-box; }
  html, body {
    width: 1200px; height: 900px; overflow: hidden;
    background: var(--stage);
  }
  .canvas { position: relative; width: 1200px; height: 900px; }

  .card {
    position: absolute;
    width: 700px; height: 400px;
    background: var(--card-yellow);
    box-shadow: 0 6px 18px rgba(0,0,0,0.18);
  }

  .brand-name {
    font-family: "Anton", "Impact", sans-serif;
    text-transform: uppercase;
    letter-spacing: 1px;
    line-height: 1;
    color: var(--ink);
  }

  /* Contact side */
  .card--contact { left: 60px; top: 45px; }
  .card--contact .brand-name {
    position: absolute; right: 50px; top: 48px;
    font-size: 66px;
    text-align: right;
  }
  .divider {
    position: absolute; left: 250px; top: 190px;
    width: 420px; height: 1px; background: var(--rule);
  }
  .services {
    position: absolute; right: 58px; top: 212px;
    list-style: none;
    font-family: "Arimo", Arial, sans-serif;
    font-size: 17px; color: var(--text-dark);
    letter-spacing: 0.5px; line-height: 26px;
  }
  .services li::before {
    content: ""; display: inline-block;
    width: 6px; height: 6px; border-radius: 50%;
    background: var(--ink);
    margin-right: 6px; vertical-align: middle;
  }
  .person { position: absolute; left: 60px; top: 204px; }
  .person__name {
    font-family: "Anton", "Impact", sans-serif;
    font-size: 34px; color: var(--ink);
    text-transform: uppercase; letter-spacing: 1px; line-height: 1.1;
  }
  .person__role {
    font-family: "Arimo", Arial, sans-serif;
    font-size: 19px; color: var(--text-dark); margin-top: 2px;
  }
  .person__rule {
    width: 185px; height: 1px; background: var(--rule); margin: 10px 0 10px;
  }
  .contacts { list-style: none; font-family: "Arimo", Arial, sans-serif; }
  .contacts li {
    display: flex; align-items: center; gap: 12px;
    font-size: 19px; color: var(--text-dark); line-height: 30px;
  }
  .contacts svg { width: 20px; height: 20px; flex: none; }

  /* Brand side */
  .card--brand {
    left: 440px; top: 455px;
    display: flex; align-items: center; justify-content: center;
  }
  .card--brand .brand-name {
    font-size: 72px; text-align: center;
  }
</style>
</head>
<body>
<main class="canvas">

  <section class="card card--contact" aria-label="Business card, contact side">
    <h1 class="brand-name">Harbor<br>Haul Away</h1>
    <div class="divider"></div>
    <ul class="services">
      <li>DONATE</li>
      <li>RECYCLE</li>
      <li>DISPOSE</li>
    </ul>
    <div class="person">
      <p class="person__name">Daniel Reyes</p>
      <p class="person__role">Manager</p>
      <div class="person__rule"></div>
      <ul class="contacts">
        <li>
          <svg viewBox="0 0 20 20" aria-hidden="true"><path fill="var(--ink)" d="M4 2.5l3 .2 1.4 3.6-1.9 1.4a9 9 0 0 0 5.8 5.8l1.4-1.9 3.6 1.4.2 3a2 2 0 0 1-2.2 1.9C8.6 17.4 2.6 11.4 2.1 4.7A2 2 0 0 1 4 2.5z"/></svg>
          555-271-8093
        </li>
        <li>
          <svg viewBox="0 0 20 20" aria-hidden="true"><rect x="1.5" y="4" width="17" height="12" rx="1" fill="var(--ink)"/><path d="M2 5l8 6 8-6" fill="none" stroke="var(--card-yellow)" stroke-width="1.4"/></svg>
          info@harborhaulaway.example
        </li>
        <li>
          <svg viewBox="0 0 20 20" aria-hidden="true"><circle cx="10" cy="10" r="8.5" fill="var(--ink)"/><path d="M1.5 10h17M10 1.5c-3 3-3 14 0 17M10 1.5c3 3 3 14 0 17" fill="none" stroke="var(--card-yellow)" stroke-width="1.2"/></svg>
          www.harborhaulaway.example
        </li>
      </ul>
    </div>
  </section>

  <section class="card card--brand" aria-label="Business card, brand side">
    <h2 class="brand-name">Harbor<br>Haul Away</h2>
  </section>

</main>
</body>
</html>
```